Bellcrest HVAC Business Card design

Looking for a modern professional two sided design. Showing contact info and services provided. Possibly on a silk card stock.
Using blues or greens or greys and maybe metallic. One color or a mixture of these.
Dorian Vance
dvance@bellcresthvac-example.net
555-318-4702
Air Conditioning
Heating
Heat Pumps / Gas / Oil
Ductless mini splits
Controls
VFD's
Pumps
Gas Fitting/Piping
Service and New install
Residential / Commercial
Industry/Entity Type
Mechanical HVAC
Contact Information for Business Card
Logo, contact info and provided services

```html
<!DOCTYPE html>
<html lang="en">
<head>
<meta charset="UTF-8">
<title>Bellcrest HVAC Business Card</title>
<link rel="stylesheet" href="https://fonts.googleapis.com/css2?family=Michroma&family=Questrial&display=swap">
<style>
  :root {
    --stage: #bdbdbd;
    --card: #6a6b6d;
    --card-edge: #5e5f61;
    --foil-light: #eeeeee;
    --foil-mid: #a9a9aa;
    --foil-dark: #2b2b2c;
    --brand-blue: #1457b8;
    --white: #ffffff;
  }
  * { box-sizing: border-box; margin: 0; padding: 0; }
  html, body { width: 1200px; height: 815px; overflow: hidden; }
  body {
    background: linear-gradient(180deg, #c9c9c9 0%, var(--stage) 100%);
    font-family: "Questrial", sans-serif;
    position: relative;
  }
  .card {
    position: absolute;
    top: 252px;
    width: 540px;
    height: 310px;
    border-radius: 22px;
    background: var(--card);
    box-shadow: 0 10px 24px rgba(0,0,0,0.28);
    overflow: hidden;
  }
  .card--front { left: 40px; }
  .card--back { left: 620px; }

  /* front */
  .brand {
    position: absolute;
    left: 34px;
    top: 62px;
    display: flex;
    align-items: center;
    gap: 12px;
  }
  .brand__dot {
    width: 34px; height: 34px;
    border-radius: 50%;
    border: 3px solid var(--foil-light);
  }
  .brand__name {
    font-family: "Questrial", sans-serif;
    font-size: 30px;
    color: var(--foil-light);
    letter-spacing: 1px;
  }
  .foil-mark {
    position: absolute;
    right: -30px;
    top: -40px;
    width: 300px;
    height: 300px;
    border-radius: 50%;
    background: radial-gradient(circle at 40% 35%, #d9d9d9 0%, #8c8c8d 40%, #2d2d2e 75%, #6a6b6d 100%);
    opacity: 0.85;
  }
  .contact {
    position: absolute;
    left: 34px;
    bottom: 40px;
  }
  .contact__name {
    font-family: "Michroma", sans-serif;
    font-size: 30px;
    color: var(--brand-blue);
    margin-bottom: 14px;
  }
  .contact__row {
    display: flex;
    align-items: center;
    gap: 10px;
    color: var(--white);
    margin-top: 8px;
  }
  .contact__row--email { font-size: 15px; }
  .contact__row--phone { font-size: 19px; font-weight: bold; letter-spacing: 0.5px; }
  .contact__icon {
    width: 22px; height: 22px;
    border-radius: 50%;
    background: var(--brand-blue);
    display: flex; align-items: center; justify-content: center;
  }

  /* back */
  .pattern-field {
    position: absolute;
    inset: 0;
    background: linear-gradient(135deg, #5d5e60 0%, #9a9a9b 35%, #4b4c4e 55%, #b4b4b5 80%, #7a7b7d 100%);
    opacity: 0.55;
  }
  .services {
    position: absolute;
    left: 190px;
    right: 18px;
    top: 142px;
    height: 128px;
    border-radius: 40px;
    background: var(--brand-blue);
    color: var(--white);
    display: flex;
    flex-direction: column;
    justify-content: center;
    align-items: center;
    font-size: 15px;
    line-height: 1.5;
    text-align: center;
  }
</style>
</head>
<body>
  <section class="card card--front" aria-label="Card front">
    <div class="foil-mark" role="img" aria-label="Large metallic foil brand emblem area"></div>
    <div class="brand">
      <span class="brand__dot"></span>
      <span class="brand__name">Bellcrest HVAC</span>
    </div>
    <div class="contact">
      <p class="contact__name">Dorian Vance</p>
      <p class="contact__row contact__row--email">
        <span class="contact__icon">
          <svg width="12" height="10" viewBox="0 0 12 10"><rect x="0.5" y="0.5" width="11" height="9" fill="none" stroke="#fff"/><path d="M0.5 0.5 L6 5.5 L11.5 0.5" fill="none" stroke="#fff"/></svg>
        </span>
        dvance@bellcresthvac-example.net
      </p>
      <p class="contact__row contact__row--phone">
        <span class="contact__icon">
          <svg width="12" height="12" viewBox="0 0 12 12"><path d="M2.5 1 L4.5 1 L5.2 3.5 L4 4.5 Q5 7 7.5 8 L8.5 6.8 L11 7.5 L11 9.5 Q10.5 11 9 11 Q1 10 1 2.5 Q1 1 2.5 1 Z" fill="#fff"/></svg>
        </span>
        555-318-4702
      </p>
    </div>
  </section>

  <section class="card card--back" aria-label="Card back">
    <div class="pattern-field" role="img" aria-label="Repeating metallic foil brand emblem pattern"></div>
    <div class="services">
      <p>• Air Conditioning • Heating • Heat Pumps / Gas / Oil</p>
      <p>• Ductless mini splits • Controls • VFD's • Pumps</p>
      <p>• Gas Fitting/Piping • Service and New install</p>
      <p>• Residential / Commercial</p>
    </div>
  </section>
</body>
</html>
```